Mobile Recording Studio needs business cards

Open to seeing a creative design, but I want to emphasis my logo and minimize the name/title and company information. Possible a fully black background on card.

My company is a mobile sound recording studio. ok to include a my trailer (actual or cartoon) on the card. My initial thought is more straight forward, but a good design will win me over.

SPECS:
CMYK color mode
High (300ppi) raster effect.
cover bleed area
please deliver: Illustrator file with layers and a pdf at completion.

Name and info for the business card:

Dallin Perry
ADR Mixer

email: Dallin@MixVault.com

address:
248 - 5170 East Hollister
Vancouver, BC V5R 2J4

phone:
604.518.2093 office

website:
www.MixVault.com

FB: @MixVault

Instagram: @TheMixVault

Industry/Entity Type

Television Production

Contact Information for Business Card

Dallin Perry
ADR Mixer

email: Dallin@MixVault.com

address:
248 - 5170 East Hollister
Vancouver, BC V5R 2J4

phone:
604.518.2093 office

website:
www.MixVault.com

FB: @MixVault

Instagram: @TheMixVault

Colors

Designer to choose colors to be used in the design.

Requirements
Must have
• emphasis my logo and minimize the name/title and company information.
• SPECS:
• CMYK color mode
• High (300ppi) raster effect.
• cover bleed area
• please deliver: Illustrator file with layers and a pdf at completion.
Nice to have
• maybe include the following:
• all black background or black theme
• my work trailer (actual or cartoon) refer to Instagram: @TheMixVault

```html
<!DOCTYPE html>
<html lang="en">
<head>
<meta charset="utf-8">
<title>MixVault Business Card</title>
<link rel="stylesheet" href="https://fonts.googleapis.com/css2?family=Cinzel:wght@400;700&family=Montserrat:wght@400;600&display=swap">
<style>
  :root {
    --stage: #2b2d32;
    --card-black: #050505;
    --card-glow: #5e5e60;
    --silver: #d8d9db;
    --silver-dim: #9a9b9e;
    --text-light: #f2f2f2;
    --text-muted: #b9babd;
    --photo-dark: #151617;
    --photo-mid: #3b3c3e;
    --photo-sky: #6b6c6e;
  }
  * { box-sizing: border-box; margin: 0; padding: 0; }
  html, body { width: 1200px; height: 900px; overflow: hidden; }
  body {
    background: var(--stage);
    display: flex;
    flex-direction: column;
    align-items: center;
    justify-content: center;
    gap: 40px;
    font-family: "Montserrat", sans-serif;
  }
  .card {
    position: relative;
    width: 700px;
    height: 400px;
    border-radius: 22px;
    overflow: hidden;
    background: var(--card-black);
  }
  /* Front */
  .card-front {
    background: radial-gradient(ellipse 360px 220px at 50% 30%, var(--card-glow) 0%, #262627 55%, var(--card-black) 100%);
  }
  .logo-word {
    position: absolute;
    top: 70px;
    left: 0;
    width: 100%;
    text-align: center;
    font-family: "Cinzel", serif;
    font-weight: 700;
    font-size: 92px;
    letter-spacing: 2px;
    color: var(--silver);
  }
  .divider {
    position: absolute;
    top: 218px;
    left: 40px;
    width: 620px;
    height: 2px;
    background: linear-gradient(90deg, transparent, var(--silver) 30%, var(--silver) 70%, transparent);
  }
  .identity {
    position: absolute;
    top: 244px;
    left: 46px;
    color: var(--text-light);
  }
  .identity .person-name {
    font-family: "Cinzel", serif;
    font-weight: 700;
    font-size: 20px;
    font-variant: small-caps;
    letter-spacing: 0.5px;
  }
  .identity .person-title {
    font-size: 13px;
    color: var(--text-muted);
    margin: 3px 0 10px;
    padding-bottom: 8px;
    border-bottom: 1px solid var(--silver-dim);
    width: 130px;
  }
  .identity .address {
    font-size: 14px;
    line-height: 1.45;
    color: var(--text-muted);
  }
  .contacts {
    position: absolute;
    top: 244px;
    right: 46px;
    list-style: none;
    color: var(--text-light);
    font-size: 15px;
  }
  .contacts li {
    display: flex;
    align-items: center;
    gap: 10px;
    height: 26px;
  }
  .contacts svg { width: 14px; height: 14px; flex: none; }
  .contacts .web strong { font-weight: 600; }
  /* Back */
  .card-back { background: var(--card-black); }
  .trailer-photo {
    position: absolute;
    inset: 0;
    background:
      linear-gradient(180deg, var(--photo-sky) 0%, var(--photo-mid) 35%, var(--photo-dark) 75%, #090909 100%);
  }
  .back-logo {
    position: absolute;
    top: 130px;
    left: 0;
    width: 100%;
    text-align: center;
    font-family: "Cinzel", serif;
    font-weight: 700;
    font-size: 110px;
    color: var(--silver);
  }
</style>
</head>
<body>

  <section class="card card-front" aria-label="Business card front">
    <div class="logo-word">MixVault</div>
    <div class="divider"></div>

    <div class="identity">
      <p class="person-name">Dallin Perry</p>
      <p class="person-title">ADR Mixer</p>
      <p class="address">248 - 5170 East Hollister<br>Vancouver, BC V5R 2J4</p>
    </div>

    <ul class="contacts">
      <li>
        <svg viewBox="0 0 16 16" aria-hidden="true"><path d="M4 1h3l1 4-2 1c1 2 2 3 4 4l1-2 4 1v3c0 1-1 2-2 2C7 14 2 9 2 3c0-1 1-2 2-2z" fill="var(--text-light)"/></svg>
        <span>604.518.2093</span>
      </li>
      <li>
        <svg viewBox="0 0 16 16" aria-hidden="true"><rect x="1" y="3" width="14" height="10" fill="none" stroke="var(--text-light)" stroke-width="1.6"/><path d="M1 3l7 6 7-6" fill="none" stroke="var(--text-light)" stroke-width="1.6"/></svg>
        <span>Dallin@MixVault.com</span>
      </li>
      <li>
        <svg viewBox="0 0 16 16" aria-hidden="true"><circle cx="8" cy="8" r="7" fill="var(--text-light)"/></svg>
        <span>@MixVault</span>
      </li>
      <li>
        <svg viewBox="0 0 16 16" aria-hidden="true"><rect x="1" y="1" width="14" height="14" fill="var(--text-light)"/></svg>
        <span>@TheMixVault</span>
      </li>
      <li class="web">
        <svg viewBox="0 0 16 16" aria-hidden="true"><circle cx="8" cy="8" r="6.5" fill="none" stroke="var(--text-light)" stroke-width="1.5"/><ellipse cx="8" cy="8" rx="3" ry="6.5" fill="none" stroke="var(--text-light)" stroke-width="1.2"/><path d="M1.5 8h13" stroke="var(--text-light)" stroke-width="1.2"/></svg>
        <span>www.<strong>MixVault</strong>.com</span>
      </li>
    </ul>
  </section>

  <section class="card card-back" aria-label="Business card back">
    <div class="trailer-photo" role="img" aria-label="Dark photo of the mobile recording studio trailer parked beside bare winter trees"></div>
    <div class="back-logo">MixVault</div>
  </section>

</body>
</html>
```